Updated Stationary needed using new logo for Hair Tissue Mineral Analysis Company

Simple stationary design needed using new logo!
1. 8.5" x 11" Letterhead with company information listed below
2. 8.5" x 11" Design with Footer only with logo and information for print materials
3. 5.5" x 8.5" letterhead design
4. 4.125" x 9.5" Business envelope (#10 envelope) with address
5. 4.125" x 9.5" Business envelope with clear window (#10 envelope) with address
6. 6.5" x 9.5" envelope (6 3/4 Booklet envelope) with address
7. 10" x 13" Open End envelope
Address:
4817 N. Corwin Street
Phoenix, AZ 85021
Phone:
(602)-417-3926
Website:
www.pexumor.com
Email:
information@pexumor.com
Updates
Need extra days to review
Focused on completing other projects first
Look and feel
Each slider illustrates characteristics of the customer's brand and the style your logo design should communicate.

```html
<!DOCTYPE html>
<html lang="en">
<head>
<meta charset="utf-8">
<title>Pexumor Labs Stationery Set</title>
<link href="https://fonts.googleapis.com/css2?family=Arimo:wght@400;700&display=swap" rel="stylesheet">
<style>
:root{
  --bg:#c9c9c9;
  --paper:#ffffff;
  --blue:#2d58a0;
  --orange:#f58220;
  --ink:#555a60;
  --shadow:2px 3px 5px rgba(0,0,0,.35);
}
*{margin:0;padding:0;box-sizing:border-box}
html,body{width:993px;height:1200px;overflow:hidden;background:var(--bg);font-family:Arimo,Arial,sans-serif}
.canvas{position:relative;width:993px;height:1200px}
.piece{position:absolute;background:var(--paper);box-shadow:var(--shadow);overflow:hidden}
.brand{position:absolute;display:flex;align-items:center;gap:4px;color:var(--blue);font-weight:700;letter-spacing:.5px;white-space:nowrap}
.brand .dot{border-radius:50%;background:var(--orange);flex:none}
.contact{position:absolute;border-left:1px solid var(--blue);color:var(--ink);line-height:1.25}
.contact li{list-style:none;display:flex;align-items:center;gap:2px}
.contact .ico{border-radius:50%;background:var(--orange);flex:none}
.footer{position:absolute;left:0;bottom:0;width:100%}
.footer svg{display:block;width:100%;height:100%}
.footer .addr{position:absolute;left:0;top:0;width:69%;height:100%;display:flex;align-items:center;justify-content:center;color:#fff}
.letter-body{position:absolute;left:32px;top:121px;width:252px;color:var(--ink)}
.letter-body .greet{font-size:7.5px;margin-bottom:12px}
.letter-body p{font-size:4.9px;line-height:6.2px;margin-bottom:6px}
.letter-body .closing{font-size:4px;margin-top:8px}
.signature{display:block;width:38px;height:11px;margin-top:8px;background:linear-gradient(90deg,#bdbdbd,#e2e2e2);border-radius:2px}
.window{position:absolute;left:27px;top:126px;width:207px;height:37px;border-radius:6px;background:linear-gradient(120deg,#b9b9b9 0%,#dcdcdc 25%,#a9a9a9 45%,#e6e6e6 65%,#b3b3b3 100%)}
.flap{position:absolute;left:0;top:0;width:100%;filter:drop-shadow(0 3px 3px rgba(0,0,0,.3))}
</style>
</head>
<body>
<div class="canvas">

<!-- Letterhead with letter -->
<section class="piece letterhead" style="left:54px;top:74px;width:315px;height:409px">
  <div class="brand" style="left:17px;top:19px;font-size:11px"><span class="dot" style="width:8px;height:8px"></span>PEXUMOR LABS</div>
  <ul class="contact" style="left:232px;top:16px;padding-left:3px;font-size:4.9px">
    <li><span class="ico" style="width:3px;height:3px"></span>(602)-417-3926</li>
    <li><span class="ico" style="width:3px;height:3px"></span>information@pexumor.com</li>
    <li><span class="ico" style="width:3px;height:3px"></span>www.pexumor.com</li>
  </ul>
  <div class="letter-body">
    <div class="greet">Dear Mr. Hale,</div>
    <p>Lorem ipsum dolor sit amet, consectetuer adipiscing elit, sed diam nonmmy nibh euismod tincidunt ut laor eet dolore magna aliquam erat volutpat. Ut wisi enim ad minim veniam, quis nostrud exerci tationmcorper suscipit lobortis nisl ut aliquip ex ea commodo consequat. Duis autem vel eum iriure dolor in hendrerit in vulputate velit esse molestie consequat, vel illum dolore eu feugiat</p>
    <p>Rorem ipsum dolor sit amet, consectetuer adipiscing elit, sed diam nonmmy nibh euismod tincidunt ut laor eet dolore magna aliquam erat volutpat. Ut wisi enim ad minim veniam, quis nostrud exerci tationmcorper suscipit lobortis nisl ut aliquip ex ea commodo consequat. Duis autem vel eum iriure dolor in hendrerit in vulputate velit esse molest</p>
    <p>Dorem ipsum dolor sit amet, consectetuer adipiscing elit, sed diam nonmmy nibh euismod tincidunt ut laor eet dolore magna aliquam erat volutpat. Ut wisi enim ad minim veniam, quis nostrud exerci tationmcorper suscipit lobortis nisl ut aliquip ex ea commodo consequat. Duis autem vel eum iriure dolor in hendrerit in suscipit lobortis nisl ut aliquip ex ea commodo consequat. Duis autem vel eum iriure dolor in hendrerit in vulputate velit esse molestie consequat, vel illum</p>
    <p>Sorem ipsum dolor sit amet, consectetuer adipiscing elit, sed diam nonmmy nibh euismod tincidunt ut laor eet dolore magna aliquam erat volutpat. Ut wisi enim ad minim veniam, quis nostrud exerci tationmcorper suscipit lobortis nisl ut aliquip ex ea commodo consequat. Duis autem vel eum iriure dolor in</p>
    <div class="closing">Sincerely,</div>
    <span class="signature" role="img" aria-label="Handwritten signature"></span>
  </div>
  <div class="footer" style="height:14px">
    <svg viewBox="0 0 552 24" preserveAspectRatio="none"><rect width="552" height="24" fill="#2d58a0"/><path d="M425 24C447 8 472 1 502 0H520C490 2 468 10 448 24Z" fill="#fff"/><path d="M448 24C470 10 490 2 520 0H552V24Z" fill="#f58220"/></svg>
    <div class="addr" style="font-size:5px">4817 N. Corwin Street, Phoenix, AZ 85021</div>
  </div>
</section>

<!-- Blank letterhead -->
<section class="piece letterhead" style="left:395px;top:74px;width:315px;height:409px">
  <div class="brand" style="left:17px;top:19px;font-size:11px"><span class="dot" style="width:8px;height:8px"></span>PEXUMOR LABS</div>
  <ul class="contact" style="left:232px;top:16px;padding-left:3px;font-size:4.9px">
    <li><span class="ico" style="width:3px;height:3px"></span>(602)-417-3926</li>
    <li><span class="ico" style="width:3px;height:3px"></span>information@pexumor.com</li>
    <li><span class="ico" style="width:3px;height:3px"></span>www.pexumor.com</li>
  </ul>
  <div class="footer" style="height:14px">
    <svg viewBox="0 0 552 24" preserveAspectRatio="none"><rect width="552" height="24" fill="#2d58a0"/><path d="M425 24C447 8 472 1 502 0H520C490 2 468 10 448 24Z" fill="#fff"/><path d="M448 24C470 10 490 2 520 0H552V24Z" fill="#f58220"/></svg>
    <div class="addr" style="font-size:5px">4817 N. Corwin Street, Phoenix, AZ 85021</div>
  </div>
</section>

<!-- Half letterhead -->
<section class="piece letterhead-small" style="left:734px;top:167px;width:204px;height:316px">
  <div class="brand" style="left:12px;top:12px;font-size:7.5px;gap:3px"><span class="dot" style="width:5px;height:5px"></span>PEXUMOR LABS</div>
  <ul class="contact" style="left:150px;top:11px;padding-left:2px;font-size:3px">
    <li><span class="ico" style="width:2px;height:2px"></span>(602)-417-3926</li>
    <li><span class="ico" style="width:2px;height:2px"></span>information@pexumor.com</li>
    <li><span class="ico" style="width:2px;height:2px"></span>www.pexumor.com</li>
  </ul>
  <div class="footer" style="height:9px">
    <svg viewBox="0 0 552 24" preserveAspectRatio="none"><rect width="552" height="24" fill="#2d58a0"/><path d="M425 24C447 8 472 1 502 0H520C490 2 468 10 448 24Z" fill="#fff"/><path d="M448 24C470 10 490 2 520 0H552V24Z" fill="#f58220"/></svg>
    <div class="addr" style="font-size:3px">4817 N. Corwin Street, Phoenix, AZ 85021</div>
  </div>
</section>

<!-- #10 envelope -->
<section class="piece envelope" style="left:54px;top:507px;width:430px;height:187px">
  <div class="brand" style="left:14px;top:15px;font-size:11px"><span class="dot" style="width:8px;height:8px"></span>PEXUMOR LABS</div>
  <div class="footer" style="height:17px">
    <svg viewBox="0 0 752 30" preserveAspectRatio="none"><rect width="752" height="30" fill="#2d58a0"/><path d="M598 30C622 12 648 2 685 0H700C668 2 640 12 620 30Z" fill="#fff"/><path d="M620 30C642 14 665 2 700 0H752V30Z" fill="#f58220"/></svg>
    <div class="addr" style="font-size:6.2px;width:100%;justify-content:flex-start;padding-left:157px">4817 N. Corwin Street, Phoenix, AZ 85021</div>
  </div>
</section>

<!-- #10 window envelope -->
<section class="piece envelope" style="left:54px;top:724px;width:430px;height:187px">
  <div class="brand" style="left:14px;top:15px;font-size:11px"><span class="dot" style="width:8px;height:8px"></span>PEXUMOR LABS</div>
  <div class="window"></div>
  <div class="footer" style="height:17px">
    <svg viewBox="0 0 752 30" preserveAspectRatio="none"><rect width="752" height="30" fill="#2d58a0"/><path d="M598 30C622 12 648 2 685 0H700C668 2 640 12 620 30Z" fill="#fff"/><path d="M620 30C642 14 665 2 700 0H752V30Z" fill="#f58220"/></svg>
    <div class="addr" style="font-size:6.2px;width:100%;justify-content:flex-start;padding-left:157px">4817 N. Corwin Street, Phoenix, AZ 85021</div>
  </div>
</section>

<!-- #10 envelope back -->
<section class="piece envelope-back" style="left:54px;top:939px;width:430px;height:187px">
  <svg class="flap" viewBox="0 0 430 54" height="54"><path d="M0 0H430L422 32Q418 51 398 51H32Q12 51 8 32Z" fill="#fff"/></svg>
  <div class="brand" style="left:144px;top:17px;font-size:11px"><span class="dot" style="width:8px;height:8px"></span>PEXUMOR LABS</div>
</section>

<!-- Booklet envelope -->
<section class="piece booklet" style="left:509px;top:507px;width:430px;height:294px">
  <div class="brand" style="left:25px;top:21px;font-size:11px"><span class="dot" style="width:8px;height:8px"></span>PEXUMOR LABS</div>
  <div class="footer" style="height:17px">
    <svg viewBox="0 0 752 30" preserveAspectRatio="none"><rect width="752" height="30" fill="#2d58a0"/><path d="M598 30C622 12 648 2 685 0H700C668 2 640 12 620 30Z" fill="#fff"/><path d="M620 30C642 14 665 2 700 0H752V30Z" fill="#f58220"/></svg>
    <div class="addr" style="font-size:6.2px;width:100%;justify-content:flex-start;padding-left:156px">4817 N. Corwin Street, Phoenix, AZ 85021</div>
  </div>
</section>

<!-- Open end envelope back -->
<section class="piece open-end" style="left:509px;top:832px;width:430px;height:294px">
  <svg class="flap" viewBox="0 0 430 54" height="54"><path d="M0 0H430L422 32Q418 51 398 51H32Q12 51 8 32Z" fill="#fff"/></svg>
  <div class="brand" style="left:144px;top:17px;font-size:11px"><span class="dot" style="width:8px;height:8px"></span>PEXUMOR LABS</div>
</section>

</div>
</body>
</html>
```